The (Private) News Sharing Report

This is a professional and academic report of 35 pages for journalists and teachers. The topic of the report is News Sharing: journalism, social networks and technology. Attached there is an example of the kind of design we are looking for: visual, fresh and modern.

Target Market(s)

Journalists, Journalism Students, Communication Researchers,

Industry/Entity Type

Media

Font styles to use
Sans Serif

Colors
3276b5
33a6d7
886aae
b868aa

Requirements
Must have
• Copyleft images, visual style
Nice to have
• There is an example attached.

```html
<!DOCTYPE html>
<html lang="en">
<head>
<meta charset="utf-8">
<title>The (Private) News Sharing Report</title>
<link rel="stylesheet" href="https://fonts.googleapis.com/css2?family=Arimo:wght@400&family=Caladea&family=Roboto:ital,wght@0,300;1,300&display=swap">
<style>
  :root {
    --blue-deep: #3276b5;
    --blue-sky: #33a6d7;
    --violet: #886aae;
    --magenta: #b868aa;
    --ink: #1c1c1c;
    --paper: #ffffff;
  }
  html, body {
    margin: 0;
    padding: 0;
    overflow: hidden;
    background: var(--paper);
  }
  .cover {
    position: relative;
    width: 848px;
    height: 1200px;
    overflow: hidden;
    background: var(--paper);
    font-family: "Arimo", Arial, sans-serif;
    color: var(--ink);
  }
  .cover-art {
    position: absolute;
    left: 0;
    top: 0;
  }
  .title-block {
    position: absolute;
    left: 0;
    top: 0;
    width: 848px;
    height: 1200px;
    pointer-events: none;
  }
  .report-title {
    position: absolute;
    left: 77px;
    top: 782px;
    transform: rotate(-90deg);
    transform-origin: left top;
    margin: 0;
    font-family: "Roboto", Arial, sans-serif;
    font-weight: 300;
    font-size: 35px;
    letter-spacing: 0.2px;
    white-space: nowrap;
    color: var(--paper);
  }
  .report-subtitle {
    position: absolute;
    left: 134px;
    top: 560px;
    transform: rotate(-90deg);
    transform-origin: left top;
    margin: 0;
    font-family: "Roboto", Arial, sans-serif;
    font-style: italic;
    font-weight: 300;
    font-size: 16.5px;
    white-space: nowrap;
    color: var(--paper);
  }
  .credits {
    position: absolute;
    right: 136px;
    top: 822px;
    margin: 0;
    text-align: right;
    font-size: 15.5px;
    line-height: 22px;
  }
  .year {
    position: absolute;
    left: 0;
    width: 948px;
    top: 910px;
    margin: 0;
    text-align: center;
    font-family: "Caladea", Georgia, serif;
    font-size: 23px;
  }
</style>
</head>
<body>
<main class="cover">
  <svg class="cover-art" width="848" height="1200" viewBox="0 0 848 1200">
    <defs>
      <linearGradient id="panelPhoto" x1="0" y1="0" x2="1" y2="0.3">
        <stop offset="0" stop-color="#c9b8de"/>
        <stop offset="0.35" stop-color="#b57ac0"/>
        <stop offset="0.6" stop-color="#4aa0da"/>
        <stop offset="1" stop-color="#8fa3d8"/>
      </linearGradient>
      <linearGradient id="panelShade" x1="0" y1="0" x2="0" y2="1">
        <stop offset="0" stop-color="#9c6bb8" stop-opacity="0.2"/>
        <stop offset="0.7" stop-color="#6a6fa6" stop-opacity="0.25"/>
        <stop offset="1" stop-color="#3f4f7c" stop-opacity="0.55"/>
      </linearGradient>
      <linearGradient id="ribbonTones" x1="0" y1="0" x2="1" y2="0">
        <stop offset="0" stop-color="#f2b48a"/>
        <stop offset="0.25" stop-color="#9fd3ea"/>
        <stop offset="0.55" stop-color="#c99bcf"/>
        <stop offset="0.8" stop-color="#93aed8"/>
        <stop offset="1" stop-color="#98cdb8"/>
      </linearGradient>
      <linearGradient id="ribbonFade" x1="0" y1="0" x2="0" y2="1">
        <stop offset="0" stop-color="#ffffff" stop-opacity="1"/>
        <stop offset="1" stop-color="#ffffff" stop-opacity="0"/>
      </linearGradient>
      <radialGradient id="peopleRing" cx="0.5" cy="0.5" r="0.5">
        <stop offset="0" stop-color="#ffffff"/>
        <stop offset="0.3" stop-color="#e9c9c9"/>
        <stop offset="0.7" stop-color="#c46a7c"/>
        <stop offset="1" stop-color="#5a8fa8"/>
      </radialGradient>
    </defs>

    <g class="side-panel" role="img" aria-label="Photograph of a press camera operator, tinted purple and blue">
      <polygon points="0,0 402,0 275,345 402,782 0,782" fill="url(#panelPhoto)"/>
      <polygon points="0,0 402,0 275,345 402,782 0,782" fill="url(#panelShade)"/>
      <polygon points="262,0 402,0 275,345" fill="#b6c9ef" opacity="0.9"/>
    </g>

    <g class="hex-gallery" role="img" aria-label="Hexagon collage: film strip, chained parcel, press photographer, presenter, world map">
      <polygon points="400,132 460,132 490,185 460,238 400,238 370,185" fill="#8a4a2a"/>
      <polygon points="575,132 635,132 665,185 635,238 575,238 545,185" fill="#6e6a66"/>
      <polygon points="400,242 460,242 490,295 460,348 400,348 370,295" fill="#7b7e86"/>
      <polygon points="575,242 635,242 665,295 635,348 575,348 545,295" fill="#6f8fb4"/>
      <rect x="484" y="205" width="60" height="80" fill="#d6d8dc"/>
    </g>

    <g class="people-circle" role="img" aria-label="Sketched ring of colourful people holding hands">
      <circle cx="513" cy="522" r="102" fill="url(#peopleRing)" opacity="0.85"/>
    </g>

    <g class="line-wave-band" role="img" aria-label="Decorative multicolour line wave pattern">
      <rect x="0" y="1010" width="848" height="190" fill="url(#ribbonTones)" opacity="0.55"/>
      <rect x="0" y="1010" width="848" height="110" fill="url(#ribbonFade)"/>
    </g>
  </svg>

  <div class="title-block">
    <h1 class="report-title">THE (PRIVATE) NEWS SHARING REPORT</h1>
    <p class="report-subtitle">A starting guide for researchers and journalists</p>
  </div>

  <p class="credits">
    A report by Lucía Herrera-Campos Visiting Scholarat the<br>
    Northgate University (Washington, D.C., USA) with the help of<br>
    Research Grants 18/19 from the Saint Elian University<br>
    (Murcia, Spain)
  </p>
  <p class="year">2019</p>
</main>
</body>
</html>
```